lifestyle website Dubai

I need to create a lifestyle website homepage design,

The top nav menu will be:
- Home
- UAE Life
- Emirates Insider
- Career Corner
- HR Essentials
- Blog Beat
- Connect with us

the homepage contents sections will be something like:

- Top Beach Clubs
- Nightlife & Eats
- Outdoor Thrills
- Shopping Spree
- Staycays
- Explore

I've attached an example for the design - but this is not my design so don't copy it.. If you could imagine an Sunwave holiday - Thats the look and feel im after.

```html
<!DOCTYPE html>
<html lang="en">
<head>
<meta charset="UTF-8">
<title>SunvibeUAE – Live Your Best UAE Lifestyle</title>
<link rel="stylesheet" href="https://fonts.googleapis.com/css2?family=Poppins:wght@400;500;600;700;800&display=swap">
<style>
:root{
  --pink:#d23bb4;
  --pink-deep:#c02aa5;
  --violet:#7a4fd6;
  --ink:#111111;
  --muted:#555555;
  --white:#ffffff;
  --footer:#000000;
  --footer-text:#e6e6e6;
}
*{margin:0;padding:0;box-sizing:border-box}
html,body{width:1200px;height:3222px;overflow:hidden;background:var(--white)}
body{font-family:"Poppins",sans-serif;color:var(--ink);position:relative}
.accent{color:var(--pink)}

/* Header */
.site-header{height:75px;display:flex;align-items:center;padding:0 62px;justify-content:space-between}
.brand{font-size:29px;font-weight:700;color:var(--pink);letter-spacing:-0.3px}
.main-nav{display:flex;align-items:center;gap:28px}
.main-nav .nav-link{font-size:13.5px;color:var(--ink);text-decoration:none}
.btn{display:inline-flex;align-items:center;justify-content:center;border-radius:30px;background:linear-gradient(90deg,var(--pink),var(--pink-deep));color:var(--white);font-weight:700;text-transform:uppercase;text-decoration:none;border:none}
.btn-contact{width:173px;height:44px;font-size:13px;margin-left:4px;color:var(--white)}

/* Hero */
.hero{position:relative;height:638px;background:linear-gradient(180deg,#4c3470 0%,#6a3f7d 40%,#8a4a9a 70%,#9a55b4 100%);color:var(--white);text-align:center}
.hero-photo{position:absolute;inset:0;background:radial-gradient(ellipse at 70% 30%,rgba(230,120,140,.45),transparent 55%),linear-gradient(90deg,rgba(40,30,60,.55),rgba(120,60,150,.15) 60%,rgba(150,70,190,.35))}
.hero-content{position:relative}
.hero h1{padding-top:162px;font-size:74px;font-weight:700;line-height:84px}
.hero h1 span{display:block;background:linear-gradient(90deg,#e04ec2,#c04fd8);-webkit-background-clip:text;background-clip:text;color:transparent}
.hero-lead{margin:26px auto 0;width:700px;font-size:17px;line-height:27px}
.hero-stats{display:flex;margin:76px 0 0 354px;text-align:left}
.stat{width:197px}
.stat strong{display:block;font-size:40px;font-weight:600;line-height:44px}
.stat span{font-size:13.5px}
.scroll-mouse{position:absolute;left:591px;top:590px;width:18px;height:28px;border:2px solid var(--white);border-radius:10px}
.scroll-mouse::after{content:"";position:absolute;left:6px;top:6px;width:2px;height:7px;background:var(--white);border-radius:2px}

/* Section headings */
.section-title{text-align:center;font-size:42px;font-weight:600;line-height:50px}
.section-sub{text-align:center;width:650px;margin:20px auto 0;font-size:14px;line-height:22px;color:var(--muted)}

/* Lifestyle */
.lifestyle{margin-top:82px}
.card-grid{display:grid;grid-template-columns:repeat(3,330px);gap:22px 24px;margin:35px 0 0 78px}
.card{position:relative;height:330px;border-radius:14px;overflow:hidden;color:var(--white);display:flex;flex-direction:column;justify-content:flex-end;padding:0 27px 26px}
.card h3{font-size:22px;font-weight:700;text-transform:uppercase;line-height:28px}
.card p{font-size:13px;line-height:16px;margin-top:6px;width:270px}
.btn-detail{width:128px;height:40px;font-size:13px;margin-top:14px;background:var(--pink)}
.card-beach{background:linear-gradient(180deg,#3fb0c6 0%,#3a8fd0 60%,#3c78d8 100%)}
.card-night{background:linear-gradient(180deg,#8a3e9a 0%,#8a46b8 55%,#7a3fd2 100%)}
.card-outdoor{background:linear-gradient(180deg,#e0b84a 0%,#eb9a3a 55%,#ef7a30 100%)}
.card-shop{background:linear-gradient(180deg,#d86a9a 0%,#d24d7e 60%,#d03e6e 100%)}
.card-stay{background:linear-gradient(180deg,#4cc7b0 0%,#35b599 60%,#27a887 100%)}
.card-explore{background:linear-gradient(180deg,#5584dc 0%,#6070d8 60%,#6a60cf 100%)}

/* Gallery */
.gallery{margin-top:110px}
.gallery-grid{display:grid;grid-template-columns:repeat(4,231px);gap:12px;margin:29px 0 0 122px}
.gallery-tile{height:231px;border-radius:4px}
.t1{background:linear-gradient(135deg,#3d8fb8,#e0a040 60%,#c85a30)}
.t2{background:linear-gradient(180deg,#f2c49a,#e4a46e 60%,#d08a58)}
.t3{background:linear-gradient(180deg,#9a7e62,#7a5a44 50%,#b0302e)}
.t4{background:linear-gradient(180deg,#3e4f72,#5a6a8a 50%,#8a5a40)}
.t5{background:linear-gradient(180deg,#b0b4bc,#7a6a58 55%,#c49a70)}
.t6{background:linear-gradient(180deg,#c8b8a6,#b89474 55%,#9a8c84)}
.t7{background:linear-gradient(180deg,#3a4e8e,#5a58b0 50%,#d04a7a)}
.t8{background:linear-gradient(180deg,#f0f2f6,#d6dae2 50%,#4a4a52)}
.btn-join{display:flex;width:172px;height:45px;margin:27px auto 0;font-size:13px}

/* Newsletter */
.newsletter{position:absolute;left:0;top:2473px;width:1200px;height:389px;background:linear-gradient(90deg,#3fcdb0 0%,#4aa8c8 40%,#6c78d8 75%,#7e52d8 100%);color:var(--white);text-align:center}
.newsletter-icon{display:block;margin:60px auto 0}
.newsletter h2{font-size:42px;font-weight:600;line-height:50px;margin-top:6px}
.newsletter p{width:650px;margin:6px auto 0;font-size:15.5px;line-height:23px}
.signup{display:flex;justify-content:center;gap:10px;margin-top:27px;padding-left:8px}
.signup-input{width:481px;height:48px;border:1px solid rgba(255,255,255,.85);border-radius:14px;background:rgba(255,255,255,.12);color:var(--white);font-family:inherit;font-size:13px;padding-left:20px}
.signup-input::placeholder{color:rgba(255,255,255,.9)}
.btn-signup{width:118px;height:48px;font-size:14px;font-family:inherit;background:var(--pink)}
.newsletter small{display:block;margin-top:24px;font-size:13px}

/* Footer */
.site-footer{position:absolute;left:0;top:2862px;width:1200px;height:360px;background:var(--footer);color:var(--footer-text)}
.footer-brand{position:absolute;left:62px;top:46px}
.footer-brand .brand{font-size:30px}
.footer-brand p{width:370px;margin-top:10px;font-size:12.5px;line-height:19.5px;color:var(--white)}
.contact-list{list-style:none;margin-top:16px}
.contact-list li{display:flex;align-items:center;gap:12px;font-size:13px;height:30px;color:var(--white)}
.footer-col{position:absolute;top:50px}
.footer-col h4{font-size:16px;font-weight:600;color:var(--white);margin-bottom:15px}
.footer-col ul{list-style:none}
.footer-col li{font-size:12.5px;line-height:26px;padding-left:2px}
.col-quick{left:544px}.col-life{left:773px}.col-support{left:995px}
.footer-rule{position:absolute;left:50px;top:298px;width:1080px;height:1px;background:#333}
.copyright{position:absolute;left:53px;top:322px;font-size:12.5px;color:var(--white)}
.social{position:absolute;right:75px;top:314px;display:flex;gap:7px}
.social span{width:36px;height:36px;border-radius:50%;background:var(--pink)}
</style>
</head>
<body>

<header class="site-header">
  <div class="brand">SunvibeUAE</div>
  <nav class="main-nav">
    <a class="nav-link" href="#">Home</a>
    <a class="nav-link" href="#">UAE Life</a>
    <a class="nav-link" href="#">Emirates Insider</a>
    <a class="nav-link" href="#">Career Corner</a>
    <a class="nav-link" href="#">HR Essentials</a>
    <a class="nav-link" href="#">Blog Beat</a>
    <a class="btn btn-contact" href="#">Contact with us</a>
  </nav>
</header>

<section class="hero">
  <div class="hero-photo" role="img" aria-label="Beach resort pool at dusk with palm trees and sun loungers under a purple tint"></div>
  <div class="hero-content">
    <h1>Live Your Best <span>UAE Lifestyle</span></h1>
    <p class="hero-lead">Discover the ultimate guide to UAE's vibrant lifestyle. From exclusive beach clubs to thrilling adventures, we've got your perfect experience covered.</p>
    <div class="hero-stats">
      <div class="stat"><strong>500+</strong><span>Experience</span></div>
      <div class="stat"><strong>50K+</strong><span>Happy Explores</span></div>
      <div class="stat"><strong>24/7</strong><span>Support</span></div>
    </div>
  </div>
  <div class="scroll-mouse"></div>
</section>

<section class="lifestyle">
  <h2 class="section-title">Your UAE <span class="accent">Lifestyle</span></h2>
  <p class="section-sub">From sunrise beach sessions to midnight adventures, discover what makes UAE the ultimate lifestyle destination for young explorers.</p>
  <div class="card-grid">
    <article class="card card-beach" role="img" aria-label="Beach club with infinity pool and palm trees">
      <h3>Top Beach Clubs</h3>
      <p>Dive into luxury at UAE's most exclusive beach clubs with infinity pools and world-class service.</p>
      <a class="btn btn-detail" href="#">View Detail</a>
    </article>
    <article class="card card-night" role="img" aria-label="City skyline at night with a rooftop crowd"><h3>Nightlife &amp; Eats</h3></article>
    <article class="card card-outdoor" role="img" aria-label="Dune buggy racing across desert sand"><h3>Outdoor Thrills</h3></article>
    <article class="card card-shop" role="img" aria-label="Bright shopping mall corridor with shoppers"><h3>Shopping Spree</h3></article>
    <article class="card card-stay" role="img" aria-label="Resort pool lined with palm trees"><h3>Staycays</h3></article>
    <article class="card card-explore" role="img" aria-label="City skyline with towers seen from a waterfront"><h3>Explore</h3></article>
  </div>
</section>

<section class="gallery">
  <h2 class="section-title">Our <span class="accent">Gallery</span></h2>
  <p class="section-sub">Follow our daily adventures and get inspired by real UAE lifestyle moments from our community</p>
  <div class="gallery-grid">
    <div class="gallery-tile t1" role="img" aria-label="Friends toasting drinks at a pool bar"></div>
    <div class="gallery-tile t2" role="img" aria-label="Sandboarding down a desert dune at sunset"></div>
    <div class="gallery-tile t3" role="img" aria-label="Handbags displayed in a mall"></div>
    <div class="gallery-tile t4" role="img" aria-label="Dinner plate on a terrace overlooking the skyline"></div>
    <div class="gallery-tile t5" role="img" aria-label="Spa massage bed by a poolside pavilion"></div>
    <div class="gallery-tile t6" role="img" aria-label="Traditional palace courtyard with a visitor"></div>
    <div class="gallery-tile t7" role="img" aria-label="Yacht party on the marina at dusk"></div>
    <div class="gallery-tile t8" role="img" aria-label="Group selfie in front of a white landmark arch"></div>
  </div>
  <a class="btn btn-join" href="#">Join Community</a>
</section>

<section class="newsletter" role="region" aria-label="Newsletter signup">
  <svg class="newsletter-icon" width="46" height="36" viewBox="0 0 46 36" fill="none" stroke="#fff" stroke-width="3">
    <rect x="2" y="2" width="42" height="32" rx="6"/>
    <path d="M4 6l19 15L42 6"/>
  </svg>
  <h2>Never Miss the Fun!</h2>
  <p>Get the latest UAE lifestyle updates, exclusive event invites, and insider tips delivered straight to your inbox.</p>
  <form class="signup">
    <input class="signup-input" type="email" placeholder="Enter Email *">
    <button class="btn btn-signup" type="button">Join Now</button>
  </form>
  <small>Join 50,000+ lifestyle enthusiasts. Unsubscribe anytime.</small>
</section>

<footer class="site-footer">
  <div class="footer-brand">
    <div class="brand">SunvibeUAE</div>
    <p>Your ultimate guide to experiencing the best of UAE lifestyle. From luxury beach clubs to thrilling adventures, we help you live your best life in the Emirates.</p>
    <ul class="contact-list">
      <li><svg width="18" height="20" viewBox="0 0 18 20"><path d="M9 1a7 7 0 0 0-7 7c0 5 7 11 7 11s7-6 7-11a7 7 0 0 0-7-7z" fill="#d23bb4"/><circle cx="9" cy="8" r="2.6" fill="#000"/></svg>Dubai, United Arb Emirates</li>
      <li><svg width="18" height="14" viewBox="0 0 18 14"><rect x="0" y="0" width="18" height="14" rx="2" fill="#d23bb4"/><path d="M1 2l8 6 8-6" stroke="#000" stroke-width="1.6" fill="none"/></svg>hello@sunvibeuae.example</li>
      <li><svg width="18" height="18" viewBox="0 0 18 18"><path d="M4 1l3 4-2 2c1 2 3 4 5 5l2-2 4 3-2 3C8 16 2 10 1 4z" fill="#d23bb4"/></svg>+000 1234 5678</li>
    </ul>
  </div>
  <div class="footer-col col-quick"><h4>Quick Links</h4><ul><li>UAE Life</li><li>Emirates Insider</li><li>Career Corner</li><li>HR Essentials</li></ul></div>
  <div class="footer-col col-life"><h4>Lifestyle</h4><ul><li>Beach Clubs</li><li>Nightlife</li><li>Adventures</li><li>Shopping</li></ul></div>
  <div class="footer-col col-support"><h4>Support</h4><ul><li>Help Center</li><li>Contact Us</li><li>Privacy Policy</li><li>Terms of Service</li></ul></div>
  <div class="footer-rule"></div>
  <div class="copyright">Copyright©2025 SunvibeUAE - All rights reserved.</div>
  <div class="social" aria-label="Social links"><span></span><span></span><span></span></div>
</footer>

</body>
</html>
```